Financial Statements templates

We are a accounting and bookkeeping firms, we are trying to change the presentation of the clients' financial statements in a more professional and interesting way using graphics and PowerPoint skills, each client should feel that his/her FS are unique and developed for him/her, first will start with the normal financial statements (Balance sheet, income statement and cash flow) and then with the financial highlights, ratios and facts where we can use the charts and graphics

Reason: More time for more ideas

Reason: I want to give more time to the participants and i did not quite liked the submitted designs so far

Target Market(s)

different industry

Industry/Entity Type

Accounting

Colors

Requirements
Must have
• We would like to have a template where we can use with different clients as we need to only update their figures and upload their logos along with our below logo i.e. kelvanoro+ as a maker/prepared by. each client should feel that their Financial Statement is customized for them.
• Should also include charts and graphics,

```html
<!DOCTYPE html>
<html lang="en">
<head>
<meta charset="utf-8">
<title>Individual Slides 01B</title>
<link href="https://fonts.googleapis.com/css2?family=Oswald:wght@500&family=Open+Sans:wght@400;600;700&display=swap" rel="stylesheet">
<style>
:root{
  --bg:#ffffff;
  --board:#8a7a5c;
  --heading:#b2afad;
  --blue:#2f66b8;
  --navy:#2c5290;
  --deep:#163570;
  --green:#7cc142;
  --green-dark:#1aa54a;
  --yellow:#f6b900;
  --orange:#f07a22;
  --charcoal:#3b3b3d;
  --grey:#6d6d70;
  --ink:#333;
}
*{margin:0;padding:0;box-sizing:border-box}
html,body{width:1200px;height:1200px;overflow:hidden;background:var(--bg)}
body{position:relative;font-family:'Open Sans',Arial,sans-serif}
.sheet-title{position:absolute;top:22px;left:0;width:1200px;text-align:center;font-family:'Oswald',sans-serif;font-weight:500;font-size:54px;letter-spacing:1px;color:var(--heading)}
.board{position:absolute;left:146px;width:895px;height:503px;background:var(--board)}
.board-top{top:126px}.board-bottom{top:660px}
.slide{position:absolute;width:239px;height:134px;background:#fff;overflow:hidden;box-shadow:0 2px 4px rgba(0,0,0,.35);color:var(--ink)}
.c1{left:53px}.c2{left:332px}.c3{left:611px}
.r1{top:24px}.r2{top:177px}.r3{top:335px}
.slide svg.body{position:absolute;inset:0;width:239px;height:134px}
.slide-title{position:absolute;left:8px;top:8px;font-size:7.5px;font-weight:700;color:var(--blue);padding-left:3px;border-left:2px solid var(--blue);line-height:9px;z-index:2}
.brand{position:absolute;right:4px;top:2px;background:#fff;padding:2px 3px;font-size:5px;font-weight:700;color:var(--navy);display:flex;align-items:center;gap:2px;z-index:2}
.brand::before{content:"";width:6px;height:6px;border-radius:50%;background:var(--navy)}
.footer{position:absolute;left:8px;bottom:3px;font-size:4px;color:#666;z-index:2}
.footer b{font-size:6px;font-weight:700;color:var(--deep)}
.page-tag{position:absolute;right:6px;bottom:4px;width:10px;height:4px;background:var(--navy);z-index:2}
.on-dark{background:var(--navy);color:#fff}
.on-dark .slide-title{color:#fff;border-color:#fff}
.on-dark .footer{background:#fff;padding:1px 3px;left:auto;right:2px;bottom:2px}
.section-green{background:var(--green)}
.section-navy{background:var(--deep)}
.section-blue{background:#2e6fb3}
.section-charcoal{background:var(--charcoal)}
.section-charcoal .slide-title{background:#fff;left:0;top:0;width:100%;padding:8px 11px 5px;border:none;height:22px}
.section-charcoal .footer{background:#fff;left:0;bottom:0;width:100%;padding:2px 8px;height:13px}
.section-label{position:absolute;right:20px;top:48px;text-align:right;color:#fff;font-weight:600;font-size:15px;line-height:18px;text-transform:uppercase}
.section-label small{display:block;font-size:4px;line-height:6px;font-weight:400;text-transform:none}
.section-green .footer,.section-navy .footer,.section-blue .footer{background:#fff;padding:1px 3px;left:auto;right:2px;bottom:2px}
.shade{position:absolute;inset:0;background:linear-gradient(120deg,rgba(255,255,255,.12) 0 30%,transparent 30% 55%,rgba(0,0,0,.06) 55%)}
.highlights-band{position:absolute;left:0;top:26px;width:100%;height:16px;background:var(--yellow)}
.highlights-art{position:absolute;left:8px;top:44px;width:80px;height:76px;border-radius:6px;background:radial-gradient(circle at 55% 45%,#fff 0 38%,#e9e9e9 40%,#cfd5d8 60%,#fff 62%)}
.highlights-text{position:absolute;right:26px;top:64px;text-align:center;font-size:14px;font-weight:700;line-height:17px;color:var(--deep)}
.city-photo{position:absolute;left:0;top:0;width:100%;height:72px;background:linear-gradient(180deg,#dfe6ee 0%,#9fb0c4 55%,#5d7088 100%)}
.about-title{position:absolute;left:18px;top:77px;font-size:9px;color:var(--navy);font-weight:600}
.about-title b{font-weight:600}
</style>
</head>
<body>

<h1 class="sheet-title">INDIVIDUAL SLIDES - 01B</h1>

<svg width="0" height="0" style="position:absolute">
  <defs>
    <symbol id="bars-four" viewBox="0 0 239 134">
      <g font-size="3.6" fill="currentColor" text-decoration="underline">
        <text x="17" y="42">Net Fixed Assets</text><text x="73" y="42">Total Current Assets</text>
        <text x="130" y="42">Total Liabilities</text><text x="183" y="42">Total Partner's Equity</text>
      </g>
      <g fill="currentColor">
        <rect x="18" y="66" width="4" height="12"/><rect x="30" y="56" width="4" height="22"/><rect x="42" y="63" width="4" height="15"/>
        <rect x="74" y="63" width="4" height="15"/><rect x="86" y="64" width="4" height="14"/><rect x="98" y="58" width="4" height="20"/>
        <rect x="130" y="64" width="4" height="14"/><rect x="142" y="62" width="4" height="16"/><rect x="154" y="56" width="4" height="22"/>
        <rect x="186" y="58" width="4" height="20"/><rect x="198" y="65" width="4" height="13"/><rect x="210" y="62" width="4" height="16"/>
        <rect x="14" y="78" width="44" height=".4"/><rect x="70" y="78" width="44" height=".4"/><rect x="126" y="78" width="44" height=".4"/><rect x="182" y="78" width="44" height=".4"/>
      </g>
      <g font-size="2.8" fill="currentColor">
        <text x="22" y="88">Net Fixed Assets</text><text x="78" y="88">Total Current</text><text x="134" y="88">Total Liabilities</text><text x="190" y="88">Total Equity</text>
        <text x="14" y="111" font-size="3.6">TOTAL LIABILITIES &amp; EQUITY</text>
        <text x="96" y="102" font-size="3.4">30-Apr-2017</text><text x="136" y="102" font-size="3.4">30-May-2017</text><text x="175" y="102" font-size="3.4">30-June-2017</text>
      </g>
      <g fill="var(--blue)"><rect x="94" y="106" width="28" height="6"/><rect x="134" y="106" width="28" height="6"/><rect x="174" y="106" width="28" height="6"/></g>
      <g font-size="3.6" fill="#fff" font-weight="700" text-anchor="middle"><text x="108" y="110.5">11,400</text><text x="148" y="110.5">11,655</text><text x="188" y="110.5">13,137</text></g>
    </symbol>
  </defs>
</svg>

<section class="board board-top">

  <article class="slide c1 r1">
    <h2 class="slide-title">H1'17 BALANCE SHEET</h2>
    <div class="brand">Avenora</div>
    <svg class="body" viewBox="0 0 239 134" style="color:var(--blue)"><use href="#bars-four"/></svg>
    <div class="footer">by <b>kelvanoro+</b></div>
  </article>

  <article class="slide c2 r1 on-dark">
    <h2 class="slide-title">H1'17 BALANCE SHEET</h2>
    <div class="brand">Avenora</div>
    <svg class="body" viewBox="0 0 239 134" style="color:#fff"><use href="#bars-four"/></svg>
    <div class="footer">by <b>kelvanoro+</b></div>
  </article>

  <article class="slide c3 r1 section-green">
    <div class="shade"></div>
    <div class="brand">Avenora</div>
    <h2 class="section-label">Income<br>Statement</h2>
    <div class="footer">by <b>kelvanoro+</b></div>
  </article>

  <article class="slide c1 r2">
    <h2 class="slide-title">INCOME STATEMENT</h2>
    <div class="brand">Avenora</div>
    <svg class="body" viewBox="0 0 239 134">
      <text x="10" y="24" font-size="2.4" fill="#888">Company income statement for the month ended June 30, 2017</text>
      <rect x="52" y="36" width="46" height="82" fill="var(--blue)"/>
      <rect x="98" y="36" width="46" height="82" fill="var(--green-dark)"/>
      <rect x="144" y="36" width="46" height="82" fill="var(--navy)"/>
      <rect x="190" y="36" width="42" height="82" fill="var(--grey)"/>
      <rect x="8" y="45" width="224" height="5.5" fill="#ffffff" opacity=".22"/>
      <rect x="8" y="45" width="44" height="5.5" fill="#d9dde3"/>
      <rect x="8" y="76" width="224" height="5" fill="#1a2f5a"/>
      <rect x="8" y="84" width="224" height="5" fill="#1a2f5a"/>
      <g font-size="3" fill="#333"><text x="10" y="32">In KWD</text><text x="66" y="32">June - 2017</text><text x="112" y="32">May - 2017</text><text x="158" y="32">Apr - 2017</text><text x="198" y="32">YTD JUNE 2017</text></g>
      <g font-size="2.6" fill="#333"><text x="10" y="49">Sales</text><text x="10" y="55">Cost of service</text><text x="10" y="61">Labor salaries</text><text x="10" y="67">Maintenance expenses</text><text x="10" y="73">Transport expenses</text></g>
      <g font-size="2.6" fill="#fff">
        <text x="56" y="41">Amount</text><text x="80" y="41">%</text><text x="102" y="41">Amount</text><text x="126" y="41">%</text><text x="148" y="41">Amount</text><text x="172" y="41">%</text><text x="194" y="41">Amount</text><text x="218" y="41">%</text>
        <text x="56" y="49">2,905</text><text x="80" y="49">100%</text><text x="102" y="49">2,905</text><text x="126" y="49">100%</text><text x="148" y="49">2,905</text><text x="172" y="49">100%</text><text x="194" y="49">17,230</text><text x="218" y="49">100%</text>
        <text x="56" y="55">287</text><text x="80" y="55">8%</text><text x="102" y="55">287</text><text x="126" y="55">8%</text><text x="148" y="55">287</text><text x="172" y="55">8%</text><text x="194" y="55">287</text><text x="218" y="55">8%</text>
        <text x="56" y="61">1,380</text><text x="80" y="61">47%</text><text x="102" y="61">1,380</text><text x="126" y="61">47%</text><text x="148" y="61">1,380</text><text x="172" y="61">47%</text><text x="194" y="61">1,380</text><text x="218" y="61">47%</text>
        <text x="56" y="67">217</text><text x="80" y="67">7%</text><text x="102" y="67">217</text><text x="126" y="67">7%</text><text x="148" y="67">217</text><text x="172" y="67">7%</text><text x="194" y="67">217</text><text x="218" y="67">7%</text>
        <text x="56" y="73">37</text><text x="80" y="73">1%</text><text x="102" y="73">37</text><text x="126" y="73">1%</text><text x="148" y="73">37</text><text x="172" y="73">1%</text><text x="194" y="73">37</text><text x="218" y="73">1%</text>
        <text x="10" y="79.8">Total Cost of Sales</text><text x="56" y="79.8">1921</text><text x="80" y="79.8">66%</text><text x="102" y="79.8">1921</text><text x="126" y="79.8">66%</text><text x="148" y="79.8">1921</text><text x="172" y="79.8">66%</text><text x="194" y="79.8">1921</text><text x="218" y="79.8">66%</text>
        <text x="10" y="87.8">Gross Profit</text><text x="56" y="87.8">984</text><text x="80" y="87.8">34%</text><text x="102" y="87.8">984</text><text x="126" y="87.8">34%</text><text x="148" y="87.8">984</text><text x="172" y="87.8">34%</text><text x="194" y="87.8">984</text><text x="218" y="87.8">34%</text>
      </g>
    </svg>
    <div class="footer">by <b>kelvanoro+</b></div><div class="page-tag"></div>
  </article>

  <article class="slide c2 r2">
    <h2 class="slide-title">GROSS PROFIT GRAPHICAL VIEW</h2>
    <div class="brand">Avenora</div>
    <svg class="body" viewBox="0 0 239 134">
      <g font-size="3" fill="#333"><text x="32" y="37">Gross Profit (Amount) for Quarter-I</text><text x="150" y="37">Gross Profit (%) for Quarter-I</text>
        <text x="40" y="94">Apr-2017</text><text x="70" y="94">May-2017</text><text x="98" y="94">June-2017</text>
        <text x="150" y="94">Apr-17</text><text x="175" y="94">May-17</text><text x="200" y="94">Jun-17</text></g>
      <g stroke="#ddd" stroke-width=".3"><line x1="22" y1="50" x2="120" y2="50"/><line x1="22" y1="62" x2="120" y2="62"/><line x1="22" y1="74" x2="120" y2="74"/><line x1="22" y1="86" x2="120" y2="86"/>
        <line x1="140" y1="50" x2="225" y2="50"/><line x1="140" y1="62" x2="225" y2="62"/><line x1="140" y1="74" x2="225" y2="74"/><line x1="140" y1="86" x2="225" y2="86"/></g>
      <polyline points="45,48 78,77 108,57" fill="none" stroke="var(--blue)" stroke-width="1"/>
      <rect x="155" y="54" width="5" height="32" fill="var(--blue)"/><rect x="180" y="81" width="5" height="5" fill="var(--blue)"/><rect x="205" y="63" width="5" height="23" fill="var(--blue)"/>
      <rect x="92" y="99" width="60" height="11" rx="3" fill="var(--yellow)"/>
      <circle cx="146" cy="104.5" r="4" fill="#fff"/><path d="M144,106 l2,-3 l2,3z" fill="var(--yellow)"/>
      <text x="96" y="106" font-size="3.2" font-weight="700" fill="#222">YTD JUNE-2017</text>
      <text x="126" y="102.5" font-size="1.9" fill="#222">AMOUNT</text>
      <text x="126" y="108" font-size="4.5" font-weight="700" fill="#222">984</text>
    </svg>
    <div class="footer">by <b>kelvanoro+</b></div><div class="page-tag"></div>
  </article>

  <article class="slide c3 r2">
    <h2 class="slide-title">INCOME STATEMENT</h2>
    <div class="brand">Avenora</div>
    <svg class="body" viewBox="0 0 239 134">
      <rect x="60" y="32" width="44" height="85" fill="var(--blue)"/>
      <rect x="104" y="32" width="44" height="85" fill="var(--green-dark)"/>
      <rect x="148" y="32" width="44" height="85" fill="var(--navy)"/>
      <rect x="192" y="32" width="42" height="85" fill="var(--grey)"/>
      <g stroke="#ffffff" stroke-opacity=".2" stroke-width=".3">
        <line x1="60" y1="42" x2="234" y2="42"/><line x1="60" y1="48" x2="234" y2="48"/><line x1="60" y1="54" x2="234" y2="54"/><line x1="60" y1="60" x2="234" y2="60"/><line x1="60" y1="66" x2="234" y2="66"/><line x1="60" y1="72" x2="234" y2="72"/><line x1="60" y1="78" x2="234" y2="78"/><line x1="60" y1="84" x2="234" y2="84"/><line x1="60" y1="90" x2="234" y2="90"/></g>
      <rect x="8" y="97" width="226" height="5" fill="#1a2f5a"/>
      <rect x="8" y="104" width="226" height="5" fill="#1a2f5a"/>
      <g font-size="3" fill="#333"><text x="10" y="30">In KWD</text><text x="72" y="30">June - 2017</text><text x="116" y="30">May - 2017</text><text x="160" y="30">Apr - 2017</text><text x="198" y="30">YTD JUNE 2017</text></g>
      <g font-size="2.6" fill="#333"><text x="10" y="40">Operating Expenses</text><text x="10" y="46">Accounting fees</text><text x="10" y="52">Bank charges</text><text x="10" y="58">Communication</text><text x="10" y="64">Depreciation</text><text x="10" y="70">Marketing</text><text x="10" y="76">Other expenses</text><text x="10" y="82">Tools expenses</text><text x="10" y="88">Uniform expense</text></g>
      <g font-size="2.6" fill="#fff">
        <text x="64" y="40">Amount</text><text x="90" y="40">%</text><text x="108" y="40">Amount</text><text x="134" y="40">%</text><text x="152" y="40">Amount</text><text x="178" y="40">%</text><text x="196" y="40">Amount</text><text x="222" y="40">%</text>
        <text x="64" y="46">200</text><text x="88" y="46">7%</text><text x="108" y="46">200</text><text x="132" y="46">7%</text><text x="152" y="46">200</text><text x="176" y="46">7%</text><text x="196" y="46">200</text><text x="220" y="46">7%</text>
        <text x="64" y="58">131</text><text x="88" y="58">4%</text><text x="108" y="58">131</text><text x="132" y="58">4%</text><text x="152" y="58">131</text><text x="176" y="58">4%</text><text x="196" y="58">131</text><text x="220" y="58">4%</text>
        <text x="64" y="70">158</text><text x="88" y="70">5%</text><text x="108" y="70">158</text><text x="132" y="70">5%</text><text x="152" y="70">158</text><text x="176" y="70">5%</text><text x="196" y="70">158</text><text x="220" y="70">5%</text>
        <text x="64" y="82">96</text><text x="88" y="82">3%</text><text x="108" y="82">96</text><text x="132" y="82">3%</text><text x="152" y="82">96</text><text x="176" y="82">3%</text><text x="196" y="82">96</text><text x="220" y="82">3%</text>
        <text x="10" y="100.8">Total Operating Expenses</text><text x="64" y="100.8">806</text><text x="88" y="100.8">28%</text><text x="108" y="100.8">806</text><text x="132" y="100.8">28%</text><text x="152" y="100.8">806</text><text x="176" y="100.8">28%</text><text x="196" y="100.8">806</text><text x="220" y="100.8">28%</text>
        <text x="10" y="107.8">Operating Profit (Loss)</text><text x="64" y="107.8">179</text><text x="88" y="107.8">6%</text><text x="108" y="107.8">179</text><text x="132" y="107.8">6%</text><text x="152" y="107.8">179</text><text x="176" y="107.8">6%</text><text x="196" y="107.8">179</text><text x="220" y="107.8">6%</text>
      </g>
      <g font-size="3.2" fill="#333"><text x="10" y="124" font-weight="700">Net Profit (Loss)</text><text x="64" y="124">179</text><text x="88" y="124">6%</text><text x="106" y="124">(1626)</text><text x="130" y="124">-57%</text><text x="152" y="124">872</text><text x="174" y="124">29%</text><text x="196" y="124">872</text><text x="220" y="124">5%</text></g>
    </svg>
  </article>

  <article class="slide c1 r3">
    <h2 class="slide-title">TOTAL OPERATING EXPENSES GRAPHICAL VIEW</h2>
    <div class="brand">Avenora</div>
    <svg class="body" viewBox="0 0 239 134">
      <g font-size="3" fill="#333"><text x="28" y="37">Total Operating Expenses (Amount) for Quarter-I</text><text x="145" y="37">Total Operating Expenses (%) for Quarter-I</text>
        <text x="40" y="94">Apr-2017</text><text x="70" y="94">May-2017</text><text x="98" y="94">June-2017</text>
        <text x="150" y="94">Apr-17</text><text x="175" y="94">May-17</text><text x="200" y="94">Jun-17</text></g>
      <g stroke="#ddd" stroke-width=".3"><line x1="22" y1="50" x2="120" y2="50"/><line x1="22" y1="62" x2="120" y2="62"/><line x1="22" y1="74" x2="120" y2="74"/><line x1="22" y1="86" x2="120" y2="86"/>
        <line x1="140" y1="50" x2="225" y2="50"/><line x1="140" y1="62" x2="225" y2="62"/><line x1="140" y1="74" x2="225" y2="74"/><line x1="140" y1="86" x2="225" y2="86"/></g>
      <polyline points="45,76 78,52 108,72" fill="none" stroke="var(--blue)" stroke-width="1"/>
      <rect x="155" y="78" width="5" height="8" fill="var(--blue)"/><rect x="180" y="54" width="5" height="32" fill="var(--blue)"/><rect x="205" y="72" width="5" height="14" fill="var(--blue)"/>
      <rect x="92" y="99" width="62" height="11" rx="3" fill="var(--yellow)"/>
      <circle cx="148" cy="104.5" r="4" fill="#fff"/><path d="M146,106 l2,-3 l2,3z" fill="var(--yellow)"/>
      <text x="96" y="106" font-size="3.2" font-weight="700" fill="#222">YTD JUNE-2017</text>
      <text x="126" y="102.5" font-size="1.9" fill="#222">AMOUNT</text>
      <text x="126" y="108" font-size="4.5" font-weight="700" fill="#222">4757</text>
    </svg>
    <div class="footer">by <b>kelvanoro+</b></div><div class="page-tag"></div>
  </article>

  <article class="slide c2 r3 on-dark">
    <h2 class="slide-title">H1'17 INCOME STATEMENT</h2>
    <div class="brand">Avenora</div>
    <svg class="body" viewBox="0 0 239 134">
      <g font-size="3.6" fill="#fff" text-decoration="underline"><text x="28" y="42">SALES</text><text x="82" y="42">Gross Profit</text><text x="134" y="42">Total Operating Expenses</text><text x="188" y="42">Operating Profit (Loss)</text></g>
      <g fill="#fff">
        <rect x="20" y="52" width="4" height="26"/><rect x="32" y="56" width="4" height="22"/><rect x="44" y="58" width="4" height="20"/>
        <rect x="76" y="52" width="4" height="26"/><rect x="88" y="66" width="4" height="12"/><rect x="100" y="58" width="4" height="20"/>
        <rect x="132" y="66" width="4" height="12"/><rect x="144" y="54" width="4" height="24"/><rect x="156" y="68" width="4" height="10"/>
        <rect x="188" y="64" width="4" height="6"/><rect x="200" y="70" width="4" height="18"/><rect x="212" y="60" width="4" height="10"/>
        <rect x="14" y="78" width="44" height=".4"/><rect x="70" y="78" width="44" height=".4"/><rect x="126" y="78" width="44" height=".4"/><rect x="182" y="70" width="44" height=".4"/>
      </g>
      <g font-size="3.4" fill="#fff"><text x="14" y="116">Net Profit (Loss)</text><text x="94" y="102">30-Apr-2017</text><text x="134" y="102">30-May-2017</text><text x="174" y="102">30-June-2017</text></g>
      <g fill="var(--blue)"><rect x="92" y="106" width="32" height="6"/><rect x="132" y="106" width="32" height="6"/><rect x="172" y="106" width="32" height="6"/></g>
      <g font-size="3" fill="#fff" font-weight="700" text-anchor="middle"><text x="108" y="110.3">872 , 29%</text><text x="148" y="110.3">(1626) , -57%</text><text x="188" y="110.3">179 , 6%</text></g>
    </svg>
    <div class="footer">by <b>kelvanoro+</b></div>
  </article>

  <article class="slide c3 r3 section-charcoal">
    <h2 class="slide-title">NET PROFIT (LOSS) INCOME STATEMENT</h2>
    <div class="brand">Avenora</div>
    <svg class="body" viewBox="0 0 239 134">
      <rect x="18" y="34" width="58" height="16" rx="8" fill="var(--blue)"/><circle cx="66" cy="42" r="6" fill="#fff"/><path d="M63,44 l3,-4 l3,4z" fill="var(--blue)"/>
      <rect x="90" y="34" width="58" height="16" rx="8" fill="var(--orange)"/><circle cx="138" cy="42" r="6" fill="#fff"/><path d="M135,40 l3,4 l3,-4z" fill="var(--orange)"/>
      <rect x="162" y="34" width="58" height="16" rx="8" fill="var(--yellow)"/><circle cx="210" cy="42" r="6" fill="#fff"/><path d="M207,44 l3,-4 l3,4z" fill="var(--yellow)"/>
      <g font-size="2" fill="#fff"><text x="28" y="39">AMOUNT</text><text x="100" y="39">AMOUNT</text><text x="172" y="39">AMOUNT</text></g>
      <g font-size="6.5" font-weight="700" fill="#fff"><text x="28" y="46.5">179</text><text x="98" y="46.5" fill="#c1121f">(1626)</text><text x="172" y="46.5">869</text></g>
      <g font-size="3.8" fill="#ddd"><text x="32" y="63">JUNE-2017</text><text x="106" y="63">MAY-2017</text><text x="180" y="63">APR-2017</text></g>
      <rect x="64" y="84" width="112" height="16" rx="3" fill="#8c8c8e"/><circle cx="162" cy="92" r="6" fill="#fff"/><path d="M159,94 l3,-4 l3,4z" fill="#8c8c8e"/>
      <text x="70" y="94" font-size="4.5" font-weight="700" fill="#fff">YTD JUNE-2017</text>
      <text x="126" y="89" font-size="2" fill="#fff">AMOUNT</text>
      <text x="126" y="96" font-size="6" font-weight="700" fill="#fff">872</text>
    </svg>
    <div class="footer">by <b>kelvanoro+</b></div>
  </article>
</section>

<section class="board board-bottom">

  <article class="slide c1 r1">
    <div class="brand">Avenora</div>
    <div class="highlights-band"></div>
    <div class="highlights-art" role="img" aria-label="Illustration of a magnifying glass over finance keywords"></div>
    <h2 class="highlights-text">FINANCIAL<br>HIGHLIGHTS</h2>
    <div class="footer">by <b>kelvanoro+</b></div><div class="page-tag"></div>
  </article>

  <article class="slide c2 r1 section-navy">
    <div class="shade"></div>
    <div class="brand">Avenora</div>
    <h2 class="section-label" style="top:44px">Financial<br>Highlights</h2>
    <div class="footer">by <b>kelvanoro+</b></div>
  </article>

  <article class="slide c3 r1">
    <h2 class="slide-title">FINANCIAL HIGHLIGHTS (SALES)</h2>
    <div class="brand">Avenora</div>
    <svg class="body" viewBox="0 0 239 134">
      <g font-size="2.6" fill="#666"><text x="8" y="28">The combined sales performance of the branches rose in the last quarter.</text><text x="8" y="32">Based on the table below each branch holds a stable average sales level.</text></g>
      <text x="52" y="42" font-size="3" fill="#333">Sales by Branch</text>
      <g stroke="#e2e2e2" stroke-width=".3"><line x1="14" y1="48" x2="108" y2="48"/><line x1="14" y1="58" x2="108" y2="58"/><line x1="14" y1="68" x2="108" y2="68"/><line x1="14" y1="78" x2="108" y2="78"/><line x1="14" y1="88" x2="108" y2="88"/></g>
      <polyline points="18,60 32,64 46,62 60,58 74,60 88,62 102,64" fill="none" stroke="var(--blue)" stroke-width=".8"/>
      <polyline points="18,64 32,70 46,64 60,66 74,80 88,66 102,70" fill="none" stroke="var(--yellow)" stroke-width=".8"/>
      <polyline points="18,66 32,62 46,68 60,62 74,66 88,64 102,66" fill="none" stroke="#7a8fb3" stroke-width=".8"/>
      <polyline points="18,62 32,66 46,66 60,70 74,64 88,68 102,62" fill="none" stroke="#b7b7b7" stroke-width=".8"/>
      <text x="150" y="41" font-size="3" fill="#333">Sales in KWD</text>
      <rect x="120" y="43" width="112" height="5" fill="var(--navy)"/>
      <g fill="#e8edf5"><rect x="120" y="48" width="112" height="4.5"/><rect x="120" y="57" width="112" height="4.5"/><rect x="120" y="66" width="112" height="4.5"/><rect x="120" y="75" width="112" height="4.5"/></g>
      <rect x="120" y="84" width="112" height="4.5" fill="var(--green)"/><rect x="120" y="88.5" width="112" height="4.5" fill="var(--green)"/>
      <rect x="120" y="93" width="72" height="9" fill="var(--deep)"/><rect x="120" y="102" width="72" height="6" fill="var(--blue)"/>
      <g font-size="2.6" fill="#333"><text x="122" y="51.5">Jan - 17</text><text x="122" y="56">Feb - 17</text><text x="122" y="60.5">Mar - 17</text><text x="122" y="65">Apr - 17</text><text x="122" y="69.5">May - 17</text><text x="122" y="74">Jun - 17</text><text x="140" y="51.5">776</text><text x="160" y="51.5">801</text><text x="182" y="51.5">1,577</text></g>
      <g font-size="2.6" fill="#fff"><text x="122" y="47">Month</text><text x="140" y="47">Branch A</text><text x="160" y="47">Branch B</text><text x="182" y="47">Total</text><text x="122" y="87.5">Total</text><text x="122" y="97">Average Sales per Month</text><text x="122" y="106">Monthly Average</text></g>
    </svg>
    <div class="footer">by <b>kelvanoro+</b></div><div class="page-tag"></div>
  </article>

  <article class="slide c1 r2">
    <h2 class="slide-title">FINANCIAL HIGHLIGHTS (SALES)</h2>
    <div class="brand">Avenora</div>
    <svg class="body" viewBox="0 0 239 134">
      <g font-size="3" fill="#333"><text x="50" y="40">Sales by Work Type</text><text x="150" y="40">Sales by Work Type</text></g>
      <g stroke="#e2e2e2" stroke-width=".3"><line x1="16" y1="46" x2="114" y2="46"/><line x1="16" y1="56" x2="114" y2="56"/><line x1="16" y1="66" x2="114" y2="66"/><line x1="16" y1="76" x2="114" y2="76"/><line x1="16" y1="86" x2="114" y2="86"/></g>
      <polyline points="20,54 36,50 52,58 68,50 84,56 100,53" fill="none" stroke="#9a9a9a" stroke-width=".8"/>
      <polyline points="20,72 36,72 52,64 68,70 84,72 100,66" fill="none" stroke="var(--blue)" stroke-width=".8"/>
      <polyline points="20,78 36,74 52,78 68,72 84,76 100,74" fill="none" stroke="var(--orange)" stroke-width=".8"/>
      <g font-size="2.4" fill="#555"><text x="18" y="92">Jan-17</text><text x="34" y="92">Feb-17</text><text x="50" y="92">Mar-17</text><text x="66" y="92">Apr-17</text><text x="82" y="92">May-17</text></g>
      <rect x="148" y="44" width="72" height="5" fill="var(--navy)"/>
      <g fill="#e8edf5"><rect x="148" y="49" width="72" height="4.5"/><rect x="148" y="58" width="72" height="4.5"/><rect x="148" y="67" width="72" height="4.5"/><rect x="148" y="76" width="72" height="4.5"/></g>
      <rect x="148" y="85" width="72" height="5" fill="var(--green)"/>
      <g font-size="2.6" fill="#fff"><text x="150" y="48">Month</text><text x="164" y="48">Normal</text><text x="180" y="48">Special</text><text x="196" y="48">VIP</text><text x="208" y="48">Total</text><text x="150" y="89">Total</text></g>
      <g font-size="2.6" fill="#333"><text x="150" y="52.5">Jan - 17</text><text x="150" y="57">Feb - 17</text><text x="150" y="61.5">Mar - 17</text><text x="150" y="66">Apr - 17</text><text x="150" y="70.5">May - 17</text><text x="150" y="75">Jun - 17</text></g>
    </svg>
    <div class="footer">by <b>kelvanoro+</b></div><div class="page-tag"></div>
  </article>

  <article class="slide c2 r2">
    <h2 class="slide-title">FINANCIAL HIGHLIGHTS (EXPENSES)</h2>
    <div class="brand">Avenora</div>
    <svg class="body" viewBox="0 0 239 134">
      <rect x="32" y="38" width="66" height="64" fill="#e9eef4" role="img" aria-label="Illustration of stacked coloured expense layers"/>
      <g fill="var(--navy)"><circle cx="124" cy="49" r="2"/><circle cx="124" cy="60" r="2"/><circle cx="124" cy="71" r="2"/><circle cx="124" cy="82" r="2"/><circle cx="124" cy="93" r="2"/><circle cx="124" cy="104" r="2"/></g>
      <g font-size="3" fill="#222" font-weight="600"><text x="130" y="49">Cost of Expenses</text><text x="130" y="60">Government Expenses &amp; Fines</text><text x="130" y="71">Marketing</text><text x="130" y="82">Uniform Expenses</text><text x="130" y="93">Other Expenses</text><text x="130" y="104">Tools Expenses</text></g>
      <g font-size="2.2" fill="#888"><text x="130" y="53">Salary costs were the main driver this period.</text><text x="130" y="64">Fees and fines paid to public bodies.</text><text x="130" y="75">Spending on campaigns rose in May.</text><text x="130" y="86">New staff uniforms were ordered.</text><text x="130" y="97">Minor items across all branches.</text><text x="130" y="108">Tools bought for field teams.</text></g>
    </svg>
    <div class="footer">by <b>kelvanoro+</b></div><div class="page-tag"></div>
  </article>

  <article class="slide c3 r2">
    <h2 class="slide-title">FINANCIAL HIGHLIGHTS (EXPENSES)</h2>
    <div class="brand">Avenora</div>
    <svg class="body" viewBox="0 0 239 134">
      <rect x="20" y="42" width="12" height="12" rx="2" fill="var(--blue)"/><rect x="118" y="42" width="12" height="12" rx="2" fill="var(--yellow)"/>
      <rect x="20" y="70" width="12" height="12" rx="2" fill="var(--orange)"/><rect x="118" y="70" width="12" height="12" rx="2" fill="#3f8fd6"/>
      <rect x="20" y="98" width="12" height="12" rx="2" fill="#8d8d8d"/><rect x="118" y="98" width="12" height="12" rx="2" fill="#4fae3a"/>
      <g fill="#fff"><circle cx="26" cy="48" r="2.5"/><circle cx="124" cy="48" r="2.5"/><circle cx="26" cy="76" r="2.5"/><circle cx="124" cy="76" r="2.5"/><circle cx="26" cy="104" r="2.5"/><circle cx="124" cy="104" r="2.5"/></g>
      <g font-size="3" fill="#222"><text x="38" y="45">Cost of Service</text><text x="136" y="45">Uniform Expenses</text><text x="38" y="73">Government Expenses &amp; Fines</text><text x="136" y="73">Other Expenses</text><text x="38" y="101">Marketing</text><text x="136" y="101">Tools Expenses</text></g>
      <g font-size="2.2" fill="#888"><text x="38" y="50">Costs held steady across the quarter.</text><text x="136" y="50">Paid for new staff uniforms.</text><text x="38" y="78">Fees paid to public bodies.</text><text x="136" y="78">Small items across branches.</text><text x="38" y="106">Campaign spend rose in May.</text><text x="136" y="106">Tools for field teams.</text></g>
    </svg>
    <div class="footer">by <b>kelvanoro+</b></div><div class="page-tag"></div>
  </article>

  <article class="slide c1 r3 section-blue">
    <div class="shade"></div>
    <div class="brand">Avenora</div>
    <h2 class="section-label" style="top:46px">Additional<br>Slide Ideas<small>- Created with sample data and images</small></h2>
    <div class="footer">by <b>kelvanoro+</b></div>
  </article>

  <article class="slide c2 r3">
    <div class="city-photo" role="img" aria-label="Photo of a city skyline with tall office towers"></div>
    <h2 class="about-title">About <b>kelvanoro+</b></h2>
    <svg class="body" viewBox="0 0 239 134">
      <g font-size="2.3" fill="#888"><text x="18" y="92">Bring your business to the next level</text><text x="18" y="100">Bring your business to the next level with</text><text x="18" y="104">strong presentation material for all</text><text x="18" y="108">business and personal reports.</text>
        <text x="148" y="84">Bring your business to the next level</text><text x="148" y="88">with strong presentation material.</text><text x="148" y="100">Bring your business to the next level</text><text x="148" y="104">with strong presentation material.</text></g>
      <g fill="var(--navy)"><rect x="128" y="84" width="12" height="1.5"/><rect x="128" y="100" width="12" height="1.5"/></g>
    </svg>
    <div class="footer">by <b>kelvanoro+</b></div><div class="page-tag"></div>
  </article>

  <article class="slide c3 r3">
    <h2 class="slide-title">OUR TEAM</h2>
    <div class="brand">Avenora</div>
    <svg class="body" viewBox="0 0 239 134">
      <text x="12" y="24" font-size="2.4" fill="#888">Meet your team here</text>
      <circle cx="42" cy="60" r="15" fill="#d9dde2" role="img" aria-label="Portrait photo of team member Rami Tolen"/>
      <circle cx="94" cy="60" r="15" fill="#3a3a3a" role="img" aria-label="Portrait photo of team member Nora Vale"/>
      <circle cx="146" cy="60" r="15" fill="#c98a3c" role="img" aria-label="Portrait photo of team member Omar Sein"/>
      <circle cx="198" cy="60" r="15" fill="#e3e6ea" role="img" aria-label="Portrait photo of team member Lina Maro"/>
      <g font-size="3" fill="var(--navy)" text-anchor="middle" letter-spacing=".5"><text x="42" y="83">★★★★</text><text x="94" y="83">★★★★</text><text x="146" y="83" fill="var(--yellow)">★★★★</text><text x="198" y="83">★★★★</text></g>
      <g font-size="3" fill="#333" text-anchor="middle"><text x="42" y="89">Rami Tolen</text><text x="94" y="89">Nora Vale</text><text x="146" y="89">Omar Sein</text><text x="198" y="89">Lina Maro</text></g>
      <g font-size="2.2" fill="#999" text-anchor="middle"><text x="42" y="94">Finance lead and senior</text><text x="94" y="94">Audit manager for all</text><text x="146" y="94">Tax advisor for local</text><text x="198" y="94">Client service lead</text></g>
      <g fill="#c7c7c7"><rect x="40" y="104" width="4" height="4"/><rect x="92" y="104" width="4" height="4"/><rect x="144" y="104" width="4" height="4"/><rect x="196" y="104" width="4" height="4"/></g>
    </svg>
    <div class="footer">by <b>kelvanoro+</b></div><div class="page-tag"></div>
  </article>
</section>

</body>
</html>
```